National Virtual accounting firm needs website designed

I need a wordpress website design for a national virtual accounting firm. I will upload my business card, logo, and postcards that I have had designed and followed the same style. I want a similar style to be followed so I can keep the running theme similar.

Services include:

Tax Services:
Tax preparation and planning services for Individuals, businesses, estates, and nonprofits
Full Service Payroll for Businesses
ODV Audit Representation

Consulting:
Entity Selection & Restructuring
Financial Projections & Forecasts
Retirement Planning
IPO Readiness

Accounting:
Bookkeeping
Reviews and Compilations
Payroll Services

Other Services:
CFO Services
Compliance Services
Controller Services
Software Implementations for Brimlane, Corvanta, and Plivorn.

Target Market(s)

small to medium size businesses, and individuals

Industry/Entity Type

accounting firms

Font styles to use
Sans Serif

Colors
59FF00
82FF00
B8FF75
E3FFCB
F4FFEA

Requirements
Must have
• Color schematics from the logo and post cards/business cards

```html
<!DOCTYPE html>
<html lang="en">
<head>
<meta charset="utf-8">
<title>Verdalio — Virtual Accounting Firm</title>
<link href="https://fonts.googleapis.com/css2?family=Poppins:wght@300;400;500;600;700;800&display=swap" rel="stylesheet">
<style>
:root{
  --green:#4cae35;
  --green-dark:#3f9b2b;
  --green-bright:#2fc21f;
  --yellow:#ffc60b;
  --mint:#eefde2;
  --mint-pale:#f4ffea;
  --ink:#111;
  --text:#333;
  --line:#c9c9c9;
  --white:#fff;
}
*{box-sizing:border-box;margin:0;padding:0}
html,body{width:1200px;height:3663px;overflow:hidden}
body{position:relative;font-family:'Poppins',sans-serif;color:var(--ink);background:var(--white)}
.abs{position:absolute}
a{color:inherit;text-decoration:none}

/* header */
.topbar{left:0;top:0;width:1200px;height:3px;background:var(--green)}
.header{left:0;top:3px;width:1200px;height:95px;background:var(--white)}
.brand{font-weight:400;color:var(--ink);font-size:34px;letter-spacing:2px;display:flex;align-items:center;gap:10px}
.brand .dot{width:18px;height:18px;border-radius:50%;background:var(--yellow)}
.header .brand{left:105px;top:30px}
.nav{left:347px;top:46px;display:flex;gap:27px;font-size:14.5px;color:var(--text)}
.nav-phone{left:790px;top:33px;display:flex;align-items:center;gap:14px;font-weight:600;font-size:15px}
.phone-ring{width:42px;height:42px;border-radius:50%;border:3px solid var(--green);display:flex;align-items:center;justify-content:center}
.btn{display:flex;align-items:center;justify-content:center;background:var(--yellow);border-radius:24px;font-weight:700;font-size:14px;color:var(--ink)}
.btn-login{left:995px;top:30px;width:100px;height:44px}

/* hero */
.hero{left:0;top:98px;width:1200px;height:600px;background:linear-gradient(90deg,#e4ece9 0%,#dfe8e5 35%,#b9c6c3 100%)}
.hero-photo{left:520px;top:98px;width:680px;height:500px;background:linear-gradient(135deg,#c7d3cf,#8d9c98 60%,#cfd6d4)}
.hero-fade{left:300px;top:98px;width:400px;height:500px;background:linear-gradient(90deg,#e2ebe8,rgba(226,235,232,0))}
.hero-title{left:104px;top:262px;font-size:38px;line-height:46px;font-weight:700;color:var(--green)}
.hero-title span{display:block;font-weight:400;color:var(--ink)}
.hero-text{left:104px;top:360px;width:330px;font-size:14px;line-height:24px;font-weight:500}
.btn-start{left:104px;top:448px;width:142px;height:42px}

/* about */
.about-bg{left:0;top:640px;width:1200px;height:720px;background:var(--mint)}
.about-photo{left:178px;top:803px;width:360px;height:360px;border-radius:50%;border:5px solid var(--yellow);background:radial-gradient(circle at 45% 40%,#8fa6c4,#35496e 70%)}
.section-title{font-size:31px;font-weight:400;letter-spacing:.5px}
.section-title b{font-weight:700;color:var(--green)}
.about-title{left:600px;top:728px}
.underline{width:240px;height:22px}
.about-underline{left:600px;top:772px}
.about-lead{left:600px;top:812px;width:497px;font-size:13.7px;line-height:27px;font-weight:600;color:var(--ink)}
.about-body{left:600px;top:928px;width:497px;font-size:13.7px;line-height:27px;color:var(--text);text-align:justify}
.btn-read{left:600px;top:1108px;width:142px;height:44px}

/* services */
.services-title{left:0;top:1340px;width:1200px;text-align:center}
.services-title b{color:var(--ink)}
.services-underline{left:495px;top:1383px}
.tabs{left:103px;top:1442px;display:flex;gap:17px}
.tab{height:74px;display:flex;align-items:center;gap:14px;padding-left:14px;background:var(--white);box-shadow:0 3px 14px rgba(0,0,0,.09);font-size:20px;color:var(--ink)}
.tab .ico{width:46px;height:46px;border-radius:50%;background:#e5f3df;display:flex;align-items:center;justify-content:center}
.tab.active{background:var(--green);color:var(--white)}
.tab.active .ico{background:#3d9b29}
.cards{left:115px;top:1585px;display:flex;gap:33px}
.card{position:relative;width:305px;height:320px;border-radius:0 0 20px 0;overflow:hidden}
.card-label{position:absolute;left:0;bottom:30px;width:100%;text-align:center;color:var(--white);font-weight:700;font-size:23px}
.card-books{background:linear-gradient(160deg,#d5dde2,#7d8c96 60%,#2f3d47)}
.card-reviews{background:linear-gradient(160deg,#b7c9b1,#6f8a6a)}
.card-payroll{background:linear-gradient(160deg,#9aa5a8,#4d5b60 60%,#2a3336)}
.card-overlay{position:absolute;left:12px;top:10px;width:283px;height:300px;background:rgba(76,174,53,.92);border-radius:0 0 18px 0;color:var(--white);text-align:center;padding:40px 22px 0}
.card-overlay h3{font-size:20px;line-height:25px;font-weight:700}
.card-overlay p{font-size:13px;line-height:25px;margin-top:12px}
.card-overlay .more{display:inline-block;margin-top:6px;font-size:13px;font-weight:700;border-bottom:2px solid var(--white);padding-bottom:3px}

/* why */
.why{left:0;top:1998px;width:1200px;height:649px;background:linear-gradient(180deg,#6dbb4a,#63b640 55%,#5aae3a)}
.why-title{left:0;top:2068px;width:1200px;text-align:center;color:var(--white);font-size:30px;font-weight:700}
.why-underline{left:475px;top:2118px}
.why-item{width:340px;text-align:center;color:var(--white)}
.why-item h3{font-size:30px;font-weight:600;letter-spacing:.5px}
.why-item p{font-size:15px;line-height:24px;margin-top:6px}
.why-circle{width:180px;height:180px;border-radius:50%;background:var(--white);display:flex;align-items:center;justify-content:center}
.why-circle .inner{width:162px;height:162px;border-radius:50%;background:var(--green-bright);display:flex;align-items:center;justify-content:center}

/* contact */
.contact-title{left:0;top:2725px;width:1200px;text-align:center}
.contact-title b{color:var(--ink)}
.contact-underline{left:475px;top:2770px}
.info{left:190px;display:flex;gap:16px}
.info .pin{width:38px;height:38px;border-radius:50%;background:var(--green);display:flex;align-items:center;justify-content:center;flex:none;margin-top:8px}
.info h4{color:var(--yellow);font-size:17px;font-weight:600}
.info p{font-size:15px;line-height:23px;color:var(--text)}
.field{border:1.5px solid var(--line);background:var(--white);font-size:14.5px;color:var(--text);padding:22px 16px 0}
.btn-submit{left:600px;top:3104px;width:142px;height:44px}

/* footer */
.footer-bg{left:0;top:3170px;width:1200px;height:493px;background:var(--mint-pale)}
.footer .brand{left:88px;top:3365px;font-size:46px}
.footer-about{left:86px;top:3452px;width:320px;font-size:13.5px;line-height:22px;color:var(--text)}
.fcol h4{font-size:20px;font-weight:500;margin-bottom:14px}
.fcol li{list-style:none;font-size:14px;line-height:30px;color:var(--text)}
.news{left:834px;top:3386px;width:286px;height:42px;border:1.5px solid var(--line);background:var(--white);font-size:13px;padding:11px 12px;color:var(--text)}
.news-btn{left:1080px;top:3386px;width:40px;height:42px;background:var(--yellow);display:flex;align-items:center;justify-content:center}
.socials{left:838px;top:3455px;display:flex;gap:6px}
.socials span{width:22px;height:22px;border-radius:50%;border:1.5px solid #555}
.socials span:first-child{background:var(--green);border-color:var(--green)}
.rule{left:84px;top:3568px;width:1032px;height:1px;background:#dfe9d7}
.copy{left:0;top:3604px;width:1200px;text-align:center;font-size:12px;color:var(--text)}
</style>
</head>
<body>

<div class="abs topbar"></div>
<header class="abs header"></header>
<div class="abs brand"><span class="dot"></span>VERDALIO</div>
<nav class="abs nav"><a>Home</a><a>About Us</a><a>Our Services</a><a>Blog</a><a>Contact Us</a></nav>
<div class="abs nav-phone">
  <span class="phone-ring"><svg width="18" height="18" viewBox="0 0 24 24"><path fill="#4cae35" d="M6.6 10.8a15.1 15.1 0 0 0 6.6 6.6l2.2-2.2c.3-.3.7-.4 1-.2 1.1.4 2.3.6 3.6.6.6 0 1 .4 1 1V20c0 .6-.4 1-1 1A17 17 0 0 1 3 4c0-.6.4-1 1-1h3.5c.6 0 1 .4 1 1 0 1.3.2 2.5.6 3.6.1.3 0 .7-.2 1z"/></svg></span>
  (555) 014-0302
</div>
<a class="abs btn btn-login">LOG IN</a>

<section class="abs hero"></section>
<div class="abs hero-photo" role="img" aria-label="Photo of a business team meeting around an office table"></div>
<div class="abs hero-fade"></div>
<h1 class="abs hero-title">WELCOME TO<span>VERDALIO</span></h1>
<p class="abs hero-text">Contact Verdalio To Discuss Your Accounting Needs, And See Just How Well America's Premier Virtual Firm Can Serve You.</p>
<a class="abs btn btn-start">GET STARTED</a>

<div class="abs about-bg"></div>
<svg class="abs" style="left:0;top:570px" width="1200" height="140" viewBox="0 0 1200 140">
  <path d="M0 130 C40 60 140 40 320 30 C620 15 900 20 1200 90 L1200 140 L0 140Z" fill="#eefde2"/>
  <path d="M0 130 C30 70 120 35 330 25 C620 10 900 15 1200 90 C900 40 620 30 330 45 C140 55 50 80 0 130Z" fill="#4cae35"/>
</svg>
<div class="abs about-photo" role="img" aria-label="Round photo of two colleagues reviewing documents"></div>
<h2 class="abs section-title about-title"><b>ABOUT</b> VERDALIO</h2>
<svg class="abs underline about-underline" viewBox="0 0 240 22"><path d="M2 20 C30 2 120 -2 238 14 C130 6 50 8 2 20Z" fill="#4cae35"/></svg>
<p class="abs about-lead">Lorem ipsum dolor sit amet, consectetur adipiscing elit, sed do eiusmod tempor incididunt ut labore et dolore magna aliqua. Ut enim ad minim veniam, quis nostrud exercitation ullamco laboris nisi ut aliquip ex ea commodo consequat.</p>
<p class="abs about-body">Sed ut perspiciatis unde omnis iste natus error sit voluptatem accusantium doloremque laudantium, totam rem aperiam, eaque ipsa quae ab illo inventore veritatis et quasi architecto beatae vitae dicta sunt explicabo. Nemo enim ipsam voluptatem quia voluptas sit aspernatur aut odit aut fugit, sed quia consequuntur magni dolores eos qui ratione voluptatem sequi nesciunt.</p>
<a class="abs btn btn-read">READ MORE</a>

<svg class="abs" style="left:0;top:1220px" width="1200" height="130" viewBox="0 0 1200 130">
  <path d="M0 130 C200 60 500 30 800 30 C1000 30 1080 20 1120 40 C1160 60 1185 85 1200 120 L1200 130Z" fill="#fff"/>
  <path d="M0 130 C200 50 500 15 800 15 C1000 15 1100 0 1150 30 C1180 50 1195 80 1200 120 C1180 85 1150 60 1110 50 C1060 38 1000 42 800 45 C500 48 220 80 0 130Z" fill="#4cae35"/>
</svg>

<h2 class="abs section-title services-title"><b>OUR</b> SERVICES</h2>
<svg class="abs underline services-underline" viewBox="0 0 240 22"><path d="M2 20 C30 2 120 -2 238 14 C130 6 50 8 2 20Z" fill="#4cae35"/></svg>

<div class="abs tabs">
  <div class="tab" style="width:220px"><span class="ico"><svg width="24" height="24" viewBox="0 0 24 24" fill="none" stroke="#333" stroke-width="1.5"><rect x="4" y="3" width="16" height="18"/><path d="M8 8h8M8 12h8M8 16h5"/></svg></span>Tax Services</div>
  <div class="tab" style="width:220px"><span class="ico"><svg width="24" height="24" viewBox="0 0 24 24" fill="none" stroke="#333" stroke-width="1.5"><circle cx="12" cy="7" r="3"/><path d="M6 20v-3a6 6 0 0 1 12 0v3M4 20h16"/></svg></span>Consulting</div>
  <div class="tab active" style="width:220px"><span class="ico"><svg width="24" height="24" viewBox="0 0 24 24" fill="none" stroke="#fff" stroke-width="1.5"><rect x="5" y="3" width="14" height="18" rx="1"/><path d="M8 7h8M8 11h2M12 11h2M8 15h2M12 15h2"/></svg></span>Accounting</div>
  <div class="tab" style="width:237px"><span class="ico"><svg width="24" height="24" viewBox="0 0 24 24" fill="none" stroke="#333" stroke-width="1.5"><path d="M4 12a8 8 0 1 1 3 6l-3 2 1-4a8 8 0 0 1-1-4z"/><path d="M9 12h.1M12 12h.1M15 12h.1" stroke-width="2.5"/></svg></span>Other Services</div>
</div>

<div class="abs cards">
  <div class="card card-books" role="img" aria-label="Photo of hands using a calculator for bookkeeping"><span class="card-label">Bookkeeping</span></div>
  <div class="card card-reviews" role="img" aria-label="Photo of an accountant reviewing financial statements">
    <div class="card-overlay">
      <h3>Reviews and<br>Compilations</h3>
      <p>Lorem ipsum dolor sit amet, consectetur adipiscing elit, sed do eiusmod tempor incididunt ut labore et dolore magna aliqua.</p>
      <span class="more">Read More</span>
    </div>
  </div>
  <div class="card card-payroll" role="img" aria-label="Photo of a laptop with payroll graphics"><span class="card-label">Payroll Services</span></div>
</div>

<section class="abs why" role="img" aria-label="Green background with soft growth imagery"></section>
<h2 class="abs why-title">WHY CHOOSE US?</h2>
<svg class="abs underline why-underline" viewBox="0 0 240 22"><path d="M2 20 C30 2 120 -2 238 14 C130 6 50 8 2 20Z" fill="#fff"/></svg>

<svg class="abs" style="left:0;top:2160px" width="1200" height="270" viewBox="0 0 1200 270" fill="none" stroke="#fff" stroke-width="2">
  <path d="M352 105 C360 160 330 200 265 210 V262"/><circle cx="265" cy="264" r="4" fill="#fff"/>
  <path d="M676 105 C684 160 654 200 590 210 V262"/><circle cx="590" cy="264" r="4" fill="#fff"/>
  <path d="M1015 105 C1023 160 993 200 930 210 V262"/><circle cx="930" cy="264" r="4" fill="#fff"/>
  <path d="M362 110 C365 85 380 75 400 74 H452"/><path d="M442 68l8 6-8 6M450 68l8 6-8 6"/>
  <path d="M690 110 C693 85 708 75 728 74 H770"/><path d="M765 68l8 6-8 6M773 68l8 6-8 6"/>
</svg>

<div class="abs why-circle" style="left:172px;top:2175px"><div class="inner">
  <svg width="96" height="80" viewBox="0 0 96 80"><rect x="2" y="16" width="92" height="62" rx="8" fill="#fff"/><path d="M32 16V8a4 4 0 0 1 4-4h24a4 4 0 0 1 4 4v8" stroke="#fff" stroke-width="6" fill="none"/><path d="M2 40h92" stroke="#2fc21f" stroke-width="4"/><rect x="38" y="34" width="20" height="14" rx="2" fill="#fff" stroke="#2fc21f" stroke-width="3"/></svg>
</div></div>
<div class="abs why-circle" style="left:498px;top:2175px"><div class="inner">
  <svg width="100" height="100" viewBox="0 0 100 100" fill="#fff"><circle cx="40" cy="24" r="18"/><path d="M6 90c0-24 14-42 34-42s34 18 34 42z"/><circle cx="72" cy="70" r="16" stroke="#2fc21f" stroke-width="4"/><circle cx="72" cy="70" r="6" fill="#2fc21f"/></svg>
</div></div>
<div class="abs why-circle" style="left:838px;top:2175px"><div class="inner">
  <svg width="80" height="100" viewBox="0 0 80 100" fill="#fff"><circle cx="40" cy="34" r="30"/><text x="40" y="46" text-anchor="middle" font-family="Poppins,sans-serif" font-weight="700" font-size="34" fill="#2fc21f">$</text><path d="M14 66h14v14h8L21 98 6 80h8zM52 66h14v14h8L59 98 44 80h8z"/></svg>
</div></div>

<div class="abs why-item" style="left:90px;top:2438px"><h3>Expirienced</h3><p>Lorem ipsum dolor sit amet, consectetur adipiscing elit, sed do eiusmod tempor incididunt.</p></div>
<div class="abs why-item" style="left:420px;top:2438px"><h3>Professional</h3><p>Lorem ipsum dolor sit amet, consectetur adipiscing elit, sed do eiusmod tempor incididunt.</p></div>
<div class="abs why-item" style="left:760px;top:2438px"><h3>Affordable</h3><p>Lorem ipsum dolor sit amet, consectetur adipiscing elit, sed do eiusmod tempor incididunt.</p></div>

<h2 class="abs section-title contact-title"><b>CONTACT</b> US</h2>
<svg class="abs underline contact-underline" viewBox="0 0 240 22"><path d="M2 20 C30 2 120 -2 238 14 C130 6 50 8 2 20Z" fill="#4cae35"/></svg>

<div class="abs info" style="top:2862px"><span class="pin"><svg width="18" height="18" viewBox="0 0 24 24"><path fill="#fff" d="M12 2a7 7 0 0 0-7 7c0 5 7 13 7 13s7-8 7-13a7 7 0 0 0-7-7zm0 9.5A2.5 2.5 0 1 1 12 6.5a2.5 2.5 0 0 1 0 5z"/></svg></span><div><h4>Location :</h4><p>P.O. Box 4410<br>Millbrook, MT 59000</p></div></div>
<div class="abs info" style="top:2958px"><span class="pin"><svg width="18" height="18" viewBox="0 0 24 24"><path fill="#fff" d="M6.6 10.8a15.1 15.1 0 0 0 6.6 6.6l2.2-2.2c.3-.3.7-.4 1-.2 1.1.4 2.3.6 3.6.6.6 0 1 .4 1 1V20c0 .6-.4 1-1 1A17 17 0 0 1 3 4c0-.6.4-1 1-1h3.5c.6 0 1 .4 1 1 0 1.3.2 2.5.6 3.6.1.3 0 .7-.2 1z"/></svg></span><div><h4>Call Us :</h4><p>(555) 014-0302</p></div></div>
<div class="abs info" style="top:3038px"><span class="pin"><svg width="18" height="18" viewBox="0 0 24 24"><path fill="#fff" d="M3 6h18v12H3zM3 6l9 7 9-7" stroke="#4cae35" stroke-width="1.5"/></svg></span><div><h4>Email Us :</h4><p>info@verdalio.com</p></div></div>

<div class="abs field" style="left:600px;top:2850px;width:214px;height:58px">First Name</div>
<div class="abs field" style="left:828px;top:2850px;width:214px;height:58px">Last Name</div>
<div class="abs field" style="left:600px;top:2923px;width:214px;height:58px">Email</div>
<div class="abs field" style="left:828px;top:2923px;width:214px;height:58px">Phone</div>
<div class="abs field" style="left:600px;top:2995px;width:442px;height:90px">Message</div>
<a class="abs btn btn-submit">SUBMIT</a>

<footer class="footer">
  <div class="abs footer-bg"></div>
  <svg class="abs" style="left:0;top:3140px" width="1200" height="140" viewBox="0 0 1200 140">
    <path d="M0 20 C40 60 120 110 400 120 C700 130 1000 80 1200 0 L1200 140 L0 140Z" fill="#f4ffea"/>
    <path d="M0 20 C50 80 150 110 400 115 C700 120 1000 70 1200 0 C1000 50 700 90 400 92 C180 93 60 70 0 20Z" fill="#4cae35"/>
  </svg>
  <div class="abs brand"><span class="dot"></span>VERDALIO</div>
  <p class="abs footer-about">Lorem ipsum dolor sit amet, consectetur adipiscing elit, sed do eiusmod tempor incididunt ut labore et dolore magna aliqua.cumsan lacus vel facilisis.</p>
  <div class="abs fcol" style="left:450px;top:3335px"><h4>Quick Link</h4><ul><li>Home</li><li>About Us</li><li>Our Services</li><li>Blog</li><li>Contact Us</li></ul></div>
  <div class="abs fcol" style="left:641px;top:3335px"><h4>Services</h4><ul><li>Tax Services</li><li>Consulting</li><li>Accounting</li><li>Other Services</li></ul></div>
  <div class="abs fcol" style="left:836px;top:3335px"><h4>Newsletter</h4></div>
  <div class="abs news">Enter Email</div>
  <div class="abs news-btn"><svg width="16" height="16" viewBox="0 0 24 24"><path fill="#111" d="M22 2 2 10l7 3 3 7z"/></svg></div>
  <div class="abs socials"><span></span><span></span><span></span><span></span></div>
  <div class="abs rule"></div>
  <p class="abs copy">©2023 Nexidra | All rights reserved | Privacy Policy | Sitemap</p>
</footer>

</body>
</html>
```